Business Card Design Project 4 Construction Business

I am after a creative, but sleek and simple/ clean business card design. This design will form the basis of future items and might include a logo or simply a creative way to lay out the text of my company name 'kestrel ventures'
I like the simplicity of black and white however I would also be happy to see a splash of colour introduced somehow to give the text some interest and make it stand out.
I would like a double sided card.
I am young (ish!) and professional, offering construction and project management services, what I don't want is the traditional builders type card featuring a cheesy hammer/ saw image etc.
As the company name, kestrel ventures, suggests, we focus on working closely and collaboratively together, in synergy with all stakeholders involved in the projects that we undertake
Construction

```html
<!DOCTYPE html>
<html lang="en">
<head>
<meta charset="utf-8">
<title>Kestrel Ventures – Business Card</title>
<link rel="stylesheet" href="https://fonts.googleapis.com/css2?family=Mulish:wght@300;400;700;800&family=Playfair+Display:ital@1&display=swap">
<style>
  :root {
    --ink: #0d0d0d;
    --paper: #ffffff;
    --backdrop: #dedede;
    --muted: #8a8a8a;
    --band-text: #e8e8e8;
  }
  * { margin: 0; padding: 0; box-sizing: border-box; }
  html, body {
    width: 1200px; height: 902px; overflow: hidden;
    background: var(--backdrop);
    font-family: "Mulish", sans-serif;
  }
  .canvas { position: relative; width: 1200px; height: 902px; }

  .card {
    position: absolute;
    width: 520px; height: 318px;
    box-shadow: 0 10px 28px rgba(0,0,0,0.18);
    overflow: hidden;
  }

  /* Back side */
  .card-back { left: 90px; top: 110px; background: var(--ink); }
  .card-back .wordmark {
    position: absolute; right: 44px; top: 132px;
    color: var(--paper);
    font-weight: 800; font-size: 30px; letter-spacing: 1px;
    text-transform: uppercase; line-height: 1;
  }
  .card-back .wordmark-mark {
    position: absolute; right: 44px; top: 172px;
    width: 10px; height: 10px; background: var(--paper);
  }
  .card-back .edge-web {
    position: absolute; left: 18px; top: 159px;
    transform: translate(-50%, -50%) rotate(-90deg);
    transform-origin: center;
    color: var(--band-text);
    font-family: "Playfair Display", serif; font-style: italic;
    font-size: 10px; letter-spacing: 0.5px; white-space: nowrap;
    margin-left: 8px;
  }

  /* Front side */
  .card-front { left: 590px; top: 470px; background: var(--paper); }
  .card-front .person {
    position: absolute; left: 0; top: 126px; width: 100%;
    text-align: center;
  }
  .person-name {
    display: inline-block; text-align: right;
    color: var(--ink);
  }
  .person-name strong {
    display: block; font-weight: 700; font-size: 21px; letter-spacing: 0.2px;
  }
  .person-name span {
    display: block; font-weight: 300; font-size: 11px; color: var(--muted);
    margin-top: 1px;
  }
  .contact-band {
    position: absolute; left: 0; right: 0; top: 230px; height: 50px;
    background: var(--ink); color: var(--band-text);
    display: flex; align-items: center; padding: 0 22px;
  }
  .contact-lines {
    flex: 1; text-align: right; font-size: 10px; line-height: 1.5;
    font-family: "Playfair Display", serif; font-style: italic;
  }
  .contact-divider {
    width: 1px; height: 30px; background: var(--band-text);
    margin: 0 14px;
  }
  .band-wordmark {
    color: var(--paper); font-weight: 800; font-size: 12px;
    text-transform: uppercase; letter-spacing: 0.6px;
  }
</style>
</head>
<body>
<main class="canvas">
  <section class="card card-back" aria-label="Card back">
    <p class="edge-web">www.kestrelventures.com.au</p>
    <p class="wordmark">Kestrel Ventures</p>
  </section>

  <section class="card card-front" aria-label="Card front">
    <div class="person">
      <p class="person-name"><strong>Owen Halvard</strong><span>Director</span></p>
    </div>
    <div class="contact-band">
      <div class="contact-lines">
        <p>Ph: 0412 555 180</p>
        <p>e-mail: owen@kestrelventures.com.au</p>
      </div>
      <span class="contact-divider"></span>
      <p class="band-wordmark">Kestrel Ventures</p>
    </div>
  </section>
</main>
</body>
</html>
```